dalewintersmyth.com
Drummer, Percussionist, Teacher, Composer
And I would like to have some sort of a logo that I can use on other things for branding.
Just wanted to add some more info. I want my site to be simple and clean. The less clicking people have to do in order to see content, the better. I like this website:
http://www.marcusfelbrook.example/
I like how simple and easy to read it is. I just would want it to be a little more modern and flashy. With pics of me and my instruments which I can provide or add later. I like the design of the template i have been using, but it is clunky. Too many things to click through to get to content. And it's not adjustable enough. Hopefully that helps clarify what I'm looking for.

```html
<!DOCTYPE html>
<html lang="en">
<head>
<meta charset="utf-8">
<title>dalewintersmyth.com</title>
<link href="https://fonts.googleapis.com/css2?family=Open+Sans:wght@300;400;600;700&display=swap" rel="stylesheet">
<style>
:root{
  --bg-dark:#2a2a2a;
  --bg-darker:#1c1c1c;
  --nav:#161616;
  --nav-active:#3a3a3a;
  --panel:#ffffff;
  --sidebar:#ececec;
  --title:#2b2b2b;
  --text:#6a6a6a;
  --meta-bg:#f0f0f0;
  --line:#dcdcdc;
  --accent:#1f7fd6;
  --accent-light:#55a9ef;
  --orange:#e0661b;
  --footer-text:#8a8a8a;
}
*{box-sizing:border-box;margin:0;padding:0}
html,body{width:1200px;height:878px;overflow:hidden}
body{
  font-family:'Open Sans',Arial,sans-serif;
  background:radial-gradient(ellipse at 50% 30%,#353535 0%,var(--bg-dark) 45%,var(--bg-darker) 100%);
  position:relative;color:var(--text);
}
.portrait{position:absolute;left:228px;top:6px;width:112px;height:150px;border-radius:40px 40px 6px 6px;
  background:linear-gradient(160deg,#d8a98a 0%,#8a6a55 35%,#2f6fb8 60%,#1b4d8c 100%)}
.brand{position:absolute;left:344px;top:6px;color:#fff;font-weight:300;font-size:52px;letter-spacing:-1px;line-height:1}
.tagline{position:absolute;left:350px;top:70px;color:var(--accent-light);font-size:12px;letter-spacing:.3px}
.search{position:absolute;left:828px;top:34px;width:220px;height:36px;border-radius:4px;background:#1a1a1a;
  box-shadow:inset 0 1px 3px #000;color:#777;font-size:12px;padding:10px 14px}
.search svg{position:absolute;right:-26px;top:8px}
.nav{position:absolute;left:343px;top:106px;width:667px;height:48px;background:var(--nav);display:flex;border-radius:3px 3px 0 0}
.nav a{color:#ddd;text-decoration:none;font-size:12.5px;padding:0 14px;line-height:48px}
.nav a.active{background:var(--nav-active);color:#fff}
.panel{position:absolute;left:192px;top:163px;width:818px;height:597px;background:var(--panel);border-radius:4px;overflow:hidden}
.sidebar{position:absolute;right:0;top:0;width:223px;height:100%;background:var(--sidebar);padding:30px 18px}
.post{position:absolute;left:19px;width:566px}
.post h2{font-size:29px;font-weight:600;color:var(--title);letter-spacing:-.5px}
.meta{height:22px;background:var(--meta-bg);margin-top:8px;font-size:10.5px;line-height:22px;padding:0 8px;position:relative;color:#555}
.meta b{font-weight:400;color:#333}
.meta .comments{margin-left:14px}
.meta .share{position:absolute;right:8px;top:3px;display:flex;gap:6px}
.meta .share span{height:16px;line-height:16px;font-size:9px;padding:0 6px;border:1px solid #c9c9c9;background:#fff;border-radius:2px}
.thumb{position:absolute;left:5px;width:151px;height:149px;border:4px solid #e3e3e3;border-radius:3px}
.thumb.drum{background:linear-gradient(135deg,#5a3a20,#c9a070 50%,#e9e4da 70%,#3a2515)}
.thumb.mallets{background:linear-gradient(150deg,#2a1a10,#8a5a30 45%,#c99a60 60%,#3a2a1a)}
.body-text{position:absolute;left:173px;width:360px;font-size:11px;line-height:15px}
.body-text p+p{margin-top:6px}
.player{position:absolute;left:173px;width:284px;height:48px;background:#f6f6f6;border:1px solid #ddd;border-radius:6px;font-size:9px;color:#777}
.readmore{position:absolute;right:-10px;background:linear-gradient(#4aa0ea,var(--accent));color:#fff;font-size:10.5px;font-weight:600;border-radius:10px;padding:3px 12px}
.rule{position:absolute;left:19px;width:576px;height:1px;background:var(--line)}
.pager{position:absolute;top:562px;left:19px;width:576px;font-size:11px;color:var(--orange)}
.pager .next{float:right}
.sidebar h3{font-size:15px;font-weight:600;color:#333;margin-bottom:10px}
.login{display:flex;gap:5px}
.login span{height:16px;flex:1;background:#fff;border:1px solid #ccc;font-size:8px;color:#999;padding:2px 4px}
.login-row{font-size:8.5px;margin-top:5px;color:#777;position:relative}
.login-row em{font-style:normal;position:absolute;right:0;top:-2px;background:var(--accent);color:#fff;padding:1px 8px;border-radius:2px}
.archives{list-style:none;margin-top:-2px}
.archives li{font-size:10.5px;color:var(--orange);line-height:19px}
.archives li::before{content:"› ";color:#999}
.sep{height:1px;background:#d0d0d0;margin:12px 0}
.mail{display:flex;gap:5px}
.mail span{flex:1;height:24px;background:#fff;border:1px solid #ccc;border-radius:12px;font-size:10px;font-style:italic;color:#aaa;padding:4px 10px}
.mail em{font-style:normal;background:var(--accent);color:#fff;font-size:10px;font-weight:700;padding:4px 8px;border-radius:3px}
.social{display:flex;gap:10px}
.social i{width:26px;height:26px;border-radius:4px;display:block}
.footer-nav{position:absolute;top:778px;left:0;width:1200px;text-align:center;font-size:11.5px;color:var(--footer-text);word-spacing:0}
.footer-nav span{margin:0 6px}
.copyright{position:absolute;top:797px;left:0;width:1200px;text-align:center;font-size:11px;color:#777}
</style>
</head>
<body>
<header>
  <div class="portrait" role="img" aria-label="Photo of the drummer holding drumsticks"></div>
  <div class="brand">dalesmyth</div>
  <div class="tagline">Drummer • Percussionist • Teacher • Composer</div>
  <div class="search">search this site...
    <svg width="18" height="20" viewBox="0 0 18 20"><circle cx="10" cy="7" r="5" fill="none" stroke="#999" stroke-width="2"/><line x1="6" y1="11" x2="1" y2="17" stroke="#999" stroke-width="2.5"/></svg>
  </div>
  <nav class="nav">
    <a class="active">Home</a><a>Drum/Percussion</a><a>Lessons</a><a>Calendar</a><a>Video</a><a>Sheet Music</a><a>MP3s</a><a>Contact Us</a>
  </nav>
</header>

<main class="panel">
  <article class="post" style="top:26px">
    <h2>Welcome to My New Website</h2>
    <div class="meta">Posted on July 06, 2011 in <b>Featured, My Point Of View</b> <span class="comments">◯ 15 Comments</span>
      <div class="share"><span>Share 37</span><span>Like 20</span></div></div>
  </article>
  <div class="thumb drum" style="top:100px" role="img" aria-label="Close-up photo of a snare drum"></div>
  <div class="player" style="top:100px">
    <svg width="284" height="48" viewBox="0 0 284 48"><circle cx="14" cy="15" r="8" fill="#ddd" stroke="#aaa"/><path d="M11 11l7 4-7 4z" fill="#555"/><circle cx="32" cy="15" r="8" fill="#ddd" stroke="#aaa"/><rect x="29" y="12" width="6" height="6" fill="#555"/><rect x="48" y="13" width="200" height="4" rx="2" fill="#ccc"/><rect x="8" y="28" width="268" height="14" rx="3" fill="#fff" stroke="#ddd"/><text x="14" y="38" font-size="8" fill="#777" font-family="Open Sans,sans-serif">practice_groove_0701.mp3</text><text x="248" y="38" font-size="8" fill="#777" font-family="Open Sans,sans-serif">0:18</text></svg>
  </div>
  <div class="body-text" style="top:172px"><p>Ah, the joys of travel. I actually enjoy browsing the SkyCart – never mind the delicious array of products for the person who already owns all the world's products; the copy alone is worth the price of admission, which is zero, since SkyCart is free. Look into it.</p></div>
  <div class="readmore" style="top:238px;left:500px;right:auto">Read More</div>
  <div class="rule" style="top:266px"></div>

  <article class="post" style="top:288px">
    <h2>Nobody Loves You Like Me</h2>
    <div class="meta">Posted on July 06, 2011 in <b>Featured, My Point Of View</b> <span class="comments">◯ 15 Comments</span>
      <div class="share"><span>Share 37</span><span>Like 20</span></div></div>
  </article>
  <div class="thumb mallets" style="top:353px" role="img" aria-label="Photo of mallets on a marimba"></div>
  <div class="body-text" style="top:358px"><p>Ah, the joys of travel. I actually enjoy browsing the SkyCart – never mind the delicious array of products for the person who already owns all the world's products; the copy alone is worth the price of admission, which is zero, since SkyCart is free. Look into it.</p>
  <p>PRESENT DAY JOGO SAYS: Um, excuse me, that is a fantastic intro – that little bass riff right before all the other instruments is CANDY. I was bracing myself for this recording to be not so good, but it's pretty decent actually.</p></div>
  <div class="readmore" style="top:507px;left:500px;right:auto">Read More</div>
  <div class="rule" style="top:534px"></div>
  <div class="pager">« Previous Entries <span class="next">Next Page »</span></div>

  <aside class="sidebar">
    <h3>Client's Login</h3>
    <div class="login"><span>Username</span><span>••••••••</span></div>
    <div class="login-row">Remember me | Forgot Password <em>Login</em></div>
    <div class="sep"></div>
    <h3>Archives</h3>
    <ul class="archives">
      <li>June 2011</li><li>May 2011</li><li>April 2011</li><li>March 2011</li><li>February 2011</li><li>January 2011</li><li>December 2010</li><li>November 2010</li><li>October 2010</li><li>September 2010</li><li>August 2010</li><li>July 2010</li><li>June 2010</li>
    </ul>
    <div class="sep"></div>
    <h3>Join our Mailing List!</h3>
    <div class="mail"><span>Enter your email address</span><em>GO</em></div>
    <div class="sep"></div>
    <h3>Follow us on</h3>
    <div class="social"><i style="background:#3b5b98"></i><i style="background:#1f7ab8"></i><i style="background:#4cb6e6"></i><i style="background:#f08a24"></i></div>
  </aside>
</main>

<footer>
  <div class="footer-nav"><span>Home</span><span>Drum/Percussion</span><span>Lessons</span><span>Calendar</span><span>Video</span><span>Sheet Music</span><span>MP3s</span><span>Contact Us</span></div>
  <div class="copyright">Copyright © 2006, dalewintersmyth.com. All rights Reserved.</div>
</footer>
</body>
</html>
```